Logo & Visitenkarte für Immobilienunternehmen
Zielgruppe
Wir sind ein Immobilienunternehmen. Wir sind tätig im Immobilienhandel, der Immobilienvermittlung und der Erstellung von Häusern.
Unsere Zielgruppe sind Personen, die eine Immobilie kaufen oder verkaufen wollen. Personen ab ca. 30 Jahren mit mittlerem bis hohem Kapital bzw. Einkommen
Aufgabenstellung
Das Design soll für Sicherheit, Vertrauen, Seriosität, Professionalität und Hochwertigkeit stehen, da es in der Immobilienbranche oft um sehr viel Geld geht.

```html
<!DOCTYPE html>
<html lang="de">
<head>
<meta charset="utf-8">
<title>Ferbin Immobilien – Visitenkarte</title>
<link rel="stylesheet" href="https://fonts.googleapis.com/css2?family=Montserrat:wght@300;500;600;700&display=swap">
<style>
  :root {
    --stage: #2a2b2d;
    --card: #ffffff;
    --brand-blue: #1577c4;
    --brand-gray: #7a7b7d;
    --ink-gray: #5c5d60;
    --rule-white: #ffffff;
  }
  * { box-sizing: border-box; margin: 0; padding: 0; }
  html, body { width: 1200px; height: 780px; overflow: hidden; }
  body {
    background: var(--stage);
    font-family: "Montserrat", sans-serif;
    position: relative;
  }
  .card {
    position: absolute;
    top: 230px;
    width: 540px;
    height: 320px;
    background: var(--card);
    border-radius: 16px;
    overflow: hidden;
  }
  .card--front { left: 40px; }
  .card--back { left: 620px; }

  .top-strip {
    position: absolute; left: 0; top: 0; right: 0;
    height: 8px;
    background: var(--brand-gray);
  }

  .brand {
    display: flex; align-items: center; gap: 8px;
    color: var(--brand-blue);
    font-weight: 600;
    letter-spacing: 0.04em;
    line-height: 1;
    white-space: nowrap;
  }
  .brand__mark {
    width: 0.42em; height: 0.42em;
    background: var(--brand-blue);
  }

  /* Front */
  .card--front .brand {
    position: absolute; left: 0; right: 0; top: 118px;
    justify-content: center;
    font-size: 38px;
  }
  .card--front .brand__sub {
    position: absolute; left: 0; right: 0; top: 164px;
    text-align: center;
    color: var(--brand-blue);
    font-size: 18px; font-weight: 600; letter-spacing: 0.2em;
  }
  .web-band {
    position: absolute; left: 0; right: 0; bottom: 0;
    height: 36px;
    background: var(--brand-blue);
    color: #fff;
    font-size: 11px; font-weight: 700; letter-spacing: 0.08em;
    display: flex; align-items: center; justify-content: flex-end;
    padding-right: 70px;
  }

  /* Back */
  .card--back .brand {
    position: absolute; right: 34px; top: 52px;
    font-size: 28px;
  }
  .card--back .brand__sub {
    position: absolute; right: 34px; top: 86px;
    color: var(--brand-blue);
    font-size: 13px; font-weight: 600; letter-spacing: 0.2em;
  }
  .person { position: absolute; left: 36px; top: 130px; }
  .person__name {
    font-size: 24px; color: var(--ink-gray); letter-spacing: 0.02em;
    font-weight: 300;
  }
  .person__name strong { font-weight: 700; }
  .person__role {
    margin-top: 4px;
    font-size: 10px; font-weight: 700; letter-spacing: 0.3em;
    color: var(--brand-blue);
    padding-left: 28px;
  }

  .contact-band {
    position: absolute; left: 0; right: 0; bottom: 0;
    height: 112px;
    background: var(--brand-blue);
    display: flex;
  }
  .contact {
    flex: 1;
    position: relative;
    padding: 44px 0 0 28px;
    color: #fff;
    font-size: 9px; font-weight: 700; letter-spacing: 0.08em; line-height: 1.4;
  }
  .contact + .contact { border-left: 1.5px solid var(--rule-white); }
  .contact__icon {
    position: absolute; left: 28px; top: -22px;
    width: 44px; height: 44px;
    border-radius: 50%;
    background: var(--card);
    border: 3px solid var(--brand-blue);
    display: flex; align-items: center; justify-content: center;
  }
  .contact__icon svg { width: 20px; height: 20px; fill: var(--ink-gray); }
</style>
</head>
<body>

<section class="card card--front" aria-label="Visitenkarte Vorderseite">
  <div class="top-strip"></div>
  <div class="brand"><span class="brand__mark"></span><span>FERBIN</span></div>
  <div class="brand__sub">IMMOBILIEN</div>
  <div class="web-band">WWW.BUSINESSNAME.COM</div>
</section>

<section class="card card--back" aria-label="Visitenkarte Rückseite">
  <div class="top-strip"></div>
  <div class="brand"><span class="brand__mark"></span><span>FERBIN</span></div>
  <div class="brand__sub">IMMOBILIEN</div>

  <div class="person">
    <div class="person__name">JOHN <strong>DOE</strong></div>
    <div class="person__role">ART DIRECTOR</div>
  </div>

  <div class="contact-band">
    <div class="contact contact--phone">
      <span class="contact__icon">
        <svg viewBox="0 0 24 24" aria-hidden="true"><path d="M6.6 10.8a15.1 15.1 0 0 0 6.6 6.6l2.2-2.2a1 1 0 0 1 1-.25 11.4 11.4 0 0 0 3.6.57 1 1 0 0 1 1 1V20a1 1 0 0 1-1 1A17 17 0 0 1 3 4a1 1 0 0 1 1-1h3.5a1 1 0 0 1 1 1c0 1.25.2 2.45.57 3.57a1 1 0 0 1-.25 1z"/></svg>
      </span>
      +00 1234 5678 9012<br>+00 1234 5678 9012
    </div>
    <div class="contact contact--address">
      <span class="contact__icon">
        <svg viewBox="0 0 24 24" aria-hidden="true"><path d="M12 2a7 7 0 0 0-7 7c0 5.2 7 13 7 13s7-7.8 7-13a7 7 0 0 0-7-7zm0 9.5A2.5 2.5 0 1 1 12 6.5a2.5 2.5 0 0 1 0 5z"/></svg>
      </span>
      123 DUMMY ROAD, LOREM<br>CITY, STATE NAME, COUNTRY
    </div>
    <div class="contact contact--web">
      <span class="contact__icon">
        <svg viewBox="0 0 24 24" aria-hidden="true"><path d="M12 2a10 10 0 1 0 0 20 10 10 0 0 0 0-20zm6.9 6h-2.9a15.6 15.6 0 0 0-1.4-3.6A8 8 0 0 1 18.9 8zM12 4c.8 1.2 1.5 2.5 1.9 4h-3.8c.4-1.5 1.1-2.8 1.9-4zM4.3 14a8 8 0 0 1 0-4h3.4a16 16 0 0 0 0 4zm.8 2h2.9c.3 1.3.8 2.5 1.4 3.6A8 8 0 0 1 5.1 16zM8 8H5.1a8 8 0 0 1 4.3-3.6C8.8 5.5 8.3 6.7 8 8zm4 12c-.8-1.2-1.5-2.5-1.9-4h3.8c-.4 1.5-1.1 2.8-1.9 4zm2.3-6H9.7a14.6 14.6 0 0 1 0-4h4.6a14.6 14.6 0 0 1 0 4zm.3 5.6c.6-1.1 1.1-2.3 1.4-3.6h2.9a8 8 0 0 1-4.3 3.6zm1.7-5.6a16 16 0 0 0 0-4h3.4a8 8 0 0 1 0 4z"/></svg>
      </span>
      WWW.BUSINESSNAME.COM<br>INFO@BUSINESSNAME.COM
    </div>
  </div>
</section>

</body>
</html>
```